Design business cards for Ironvale Barbers (Opening March so won't need finalised till January2018

Ironvale Barbers is the new age barbers and skincare for all men. Creating tailor made haircuts & customised skincare solutions for the perfect healthy manly look. The Barbers will have a industrial, rustic, worldly feel about it. Rustic red brick wall with old wine barrels as the work stations with the old fashion barber chairs. Concrete floor and a bit corrugated iron around.
Target Market(s)
Professional males who like a great haircut, wet shave and may consider a facial if in the right environment. Total pampering experience in a boys environment.
Industry/Entity Type
Barber
Contact Information for Business Card
Front- Logo - address is 42 Kowhai Rd Taupo
Ph - (07) 348 6192
www.ironvalebarbers.com
email - hello@ironvale.co.nz
Back of card
Mens Haircare - Wet Shaving - Facials - Skin Prescriptions
We are doing a loyalty program - 6 squares numbered then 7th free
Colors
Designer to choose colors to be used in the design.
Requirements
Must have
- Clean simple easy to read.
Nice to have
- Our current colours are white font on black background but thinking we need to introduce another colour. Maybe white logo on a copper, bronze or rusty background. Or even a rustic red brick wall with white writing. Want it clean simple to read. Maybe a burgundy?
Should not have
- no images like heads, scissors, razors please

```html
<!DOCTYPE html>
<html lang="en">
<head>
<meta charset="utf-8">
<title>Ironvale Barbers – Business Cards</title>
<link rel="stylesheet" href="https://fonts.googleapis.com/css2?family=Anton&family=Bebas+Neue&family=Cinzel:wght@600;700&display=swap">
<style>
  :root {
    --backdrop: #5b4738;
    --card-white: #ffffff;
    --ink: #111111;
    --timber-light: #9a8469;
    --timber-mid: #7f6a52;
    --timber-dark: #5f4d3a;
    --burnt-ink: #2f2417;
  }
  * { margin: 0; padding: 0; box-sizing: border-box; }
  html, body { width: 1200px; height: 960px; overflow: hidden; }
  body { background: var(--backdrop); position: relative; }

  .card { position: absolute; width: 600px; height: 342px; box-shadow: 2px 3px 6px rgba(0,0,0,.45); }

  /* Front */
  .card-front { left: 314px; top: 113px; background: var(--card-white); color: var(--ink); }
  .holder-name {
    position: absolute; left: 40px; top: 20px;
    font-family: "Anton", sans-serif; font-size: 64px; line-height: 1; letter-spacing: .5px;
    transform: scaleY(1.02);
  }
  .name-divider { position: absolute; left: 440px; top: 28px; width: 2px; height: 66px; background: var(--ink); }
  .mobile { position: absolute; left: 462px; top: 24px; font-family: "Bebas Neue", sans-serif; line-height: 1; }
  .mobile-prefix { display: block; font-size: 26px; }
  .mobile-number { display: block; font-size: 46px; margin-top: 2px; }
  .rule { position: absolute; left: 40px; width: 512px; height: 2px; background: var(--ink); }
  .rule-1 { top: 94px; } .rule-2 { top: 146px; } .rule-3 { top: 229px; }
  .address {
    position: absolute; left: 40px; width: 512px; top: 108px; text-align: center;
    font-family: "Cinzel", serif; font-weight: 700; font-size: 20px; letter-spacing: 1px;
  }
  .web-contacts {
    position: absolute; left: 40px; width: 512px; top: 154px; text-align: center;
    font-family: "Cinzel", serif; font-weight: 600; font-size: 29px; line-height: 31px; letter-spacing: 2px;
  }
  .services {
    position: absolute; left: 40px; width: 520px; top: 250px;
    font-family: "Bebas Neue", sans-serif; font-size: 25.5px; letter-spacing: .2px; white-space: nowrap;
  }
  .appointment {
    position: absolute; left: 40px; top: 289px; display: flex; align-items: flex-end;
    font-family: "Bebas Neue", sans-serif; font-size: 28px; line-height: 1;
  }
  .blank { display: inline-block; height: 3px; background: var(--ink); margin: 0 2px 4px 3px; }
  .blank-date { width: 210px; } .blank-time { width: 212px; }

  /* Back */
  .card-back { left: 312px; top: 472px; }
  .timber {
    position: absolute; inset: 0;
    background: linear-gradient(90deg, var(--timber-mid), var(--timber-light) 30%, var(--timber-mid) 55%, var(--timber-light) 80%, var(--timber-dark));
  }
  .brand {
    position: absolute; left: 0; right: 0; top: 84px; text-align: center;
    font-family: "Anton", sans-serif; color: var(--burnt-ink); line-height: 1;
  }
  .brand-main { display: block; font-size: 104px; letter-spacing: 2px; }
  .brand-sub { display: block; font-size: 34px; letter-spacing: 9px; margin-top: 8px; }
</style>
</head>
<body>
  <section class="card card-front" aria-label="Card front">
    <h1 class="holder-name">LIAM CARTER</h1>
    <span class="name-divider"></span>
    <p class="mobile"><span class="mobile-prefix">027 583</span><span class="mobile-number">2946</span></p>
    <span class="rule rule-1"></span>
    <p class="address">42 Kowhai Rd Taupo</p>
    <span class="rule rule-2"></span>
    <p class="web-contacts">HELLO@IRONVALE.CO.NZ<br>IRONVALEBARBERS.CO.NZ</p>
    <span class="rule rule-3"></span>
    <p class="services">MENS HAIRCARE - WET SHAVING - FACIALS - SKIN PRESCRIPTIONS</p>
    <p class="appointment">DATE<span class="blank blank-date"></span>TIME<span class="blank blank-time"></span></p>
  </section>

  <section class="card card-back" aria-label="Card back">
    <div class="timber" role="img" aria-label="Weathered timber plank texture"></div>
    <p class="brand"><span class="brand-main">IRONVALE</span><span class="brand-sub">BARBERS</span></p>
  </section>
</body>
</html>
```